Awesome Business Card Design needed!

Hey there.
I'm looking for a simple but awesome business card design.
Type of company: Online advertisement agency
(please don't use the typical business people or statistics images on the card)
The front has to display the business name
and possibly some sort of logo ( perhaps something with the two M's of the biz name )
And the back of the card should say:
Name
Phone
Email
Let your imagination flow.
here are some designs that I like and that you can use as inspiration.
Simple but Awesome
http://images.pixelvantor.net/designs/55128_877673_43091_thumbnail.jpg
http://images.pixelvantor.net/designs/37714_747642_40106_image.jpg
http://images.pixelvantor.net/designs/55128_877673_43091_image.jpg
http://images.pixelvantor.net/designs/51321_781878_43091_image.jpg
http://images.pixelvantor.net/designs/33378_399063_15912_image.jpg
http://images.pixelvantor.net/designs/2337_271604_9495_image.jpg
good luck

```html
<!DOCTYPE html>
<html lang="en">
<head>
<meta charset="utf-8">
<title>Veldora Media – Business Card</title>
<link rel="stylesheet" href="https://fonts.googleapis.com/css2?family=Cinzel:wght@400&family=Crimson+Text:wght@400&family=Open+Sans:wght@400&display=swap">
<style>
  :root {
    --bg: #ecebe8;
    --card-black: #060807;
    --card-gloss: #333535;
    --card-white: #ffffff;
    --teal: #1490ae;
    --teal-light: #72cde0;
    --ink: #141414;
    --tagline-grey: #b9b9b9;
  }
  * { margin: 0; padding: 0; box-sizing: border-box; }
  html, body {
    width: 1200px;
    height: 900px;
    overflow: hidden;
    background: var(--bg);
  }
  .stage {
    position: relative;
    width: 1200px;
    height: 900px;
    display: flex;
    flex-direction: column;
    align-items: center;
    justify-content: center;
    gap: 48px;
  }
  .card {
    position: relative;
    width: 640px;
    height: 366px;
    border-radius: 26px;
    overflow: hidden;
    box-shadow: 0 10px 24px rgba(0, 0, 0, 0.18);
  }

  /* Front */
  .card-front {
    background: var(--card-black);
  }
  .card-front .gloss {
    position: absolute;
    inset: 0;
    background: radial-gradient(ellipse 120% 95% at 20% -10%, var(--card-gloss) 0 62%, transparent 62.4%);
  }
  .brand {
    position: absolute;
    display: flex;
    flex-direction: column;
    align-items: center;
  }
  .card-front .brand {
    left: 0; right: 0;
    top: 104px;
  }
  .brand-mark {
    width: 62px;
    height: 62px;
    border-radius: 50%;
    background: var(--teal-light);
    margin-bottom: 18px;
  }
  .brand-name {
    font-family: "Cinzel", "Times New Roman", serif;
    font-weight: 400;
    font-size: 40px;
    letter-spacing: 1px;
    line-height: 1;
    color: var(--teal-light);
  }
  .brand-tagline {
    font-family: "Crimson Text", "Times New Roman", serif;
    font-size: 21px;
    line-height: 1.1;
    margin-top: 4px;
  }
  .card-front .brand-tagline { color: var(--tagline-grey); }

  /* Back */
  .card-back {
    background: var(--card-white);
  }
  .card-back .brand {
    left: 44px;
    top: 136px;
    align-items: flex-start;
  }
  .card-back .brand-mark {
    background: var(--teal);
    width: 54px;
    height: 54px;
    margin-bottom: 16px;
  }
  .card-back .brand-name {
    font-size: 32px;
    color: var(--teal);
  }
  .card-back .brand-tagline {
    color: var(--ink);
    font-size: 19px;
  }
  .person {
    position: absolute;
    left: 402px;
    top: 62px;
  }
  .person-name {
    font-family: "Crimson Text", "Times New Roman", serif;
    font-size: 34px;
    line-height: 1;
    color: var(--teal);
  }
  .person-role {
    font-family: "Crimson Text", "Times New Roman", serif;
    font-size: 18px;
    color: var(--ink);
    margin-top: 2px;
  }
  .contact {
    position: absolute;
    left: 402px;
    top: 160px;
    list-style: none;
    font-family: "Open Sans", Arial, sans-serif;
    font-size: 15px;
    color: var(--ink);
  }
  .contact li {
    display: flex;
    align-items: center;
    gap: 10px;
    margin-bottom: 10px;
  }
  .contact svg { width: 16px; height: 16px; fill: var(--teal); }
  .edge-band {
    position: absolute;
    left: 0; right: 0; bottom: 0;
    height: 26px;
    display: flex;
  }
  .edge-band .band-main { flex: 1; background: var(--teal); }
  .edge-band .band-end { width: 76px; background: var(--teal-light); }
</style>
</head>
<body>
<main class="stage">
  <section class="card card-front" aria-label="Card front">
    <div class="gloss"></div>
    <div class="brand">
      <span class="brand-mark"></span>
      <span class="brand-name">VELDORA MEDIA</span>
      <span class="brand-tagline">Online advertisement agency</span>
    </div>
  </section>

  <section class="card card-back" aria-label="Card back">
    <div class="brand">
      <span class="brand-mark"></span>
      <span class="brand-name">VELDORA MEDIA</span>
      <span class="brand-tagline">Online advertisement agency</span>
    </div>
    <div class="person">
      <p class="person-name">Your Name</p>
      <p class="person-role">Company Position</p>
    </div>
    <ul class="contact">
      <li>
        <svg viewBox="0 0 16 16" aria-hidden="true"><path d="M1 3h14v10H1z M1.5 3.5 8 9l6.5-5.5" fill="var(--teal)" stroke="#fff" stroke-width="1"/></svg>
        <span>name@domainname.com</span>
      </li>
      <li>
        <svg viewBox="0 0 16 16" aria-hidden="true"><path d="M4.2 1.5 6.3 4.6 4.9 6.1c.8 2 2.6 3.9 4.8 4.9l1.4-1.4 3.1 2.1-1.4 2.3C8 14.2 1.6 7.9 1.9 2.9z"/></svg>
        <span>000 000 0000</span>
      </li>
    </ul>
    <div class="edge-band">
      <span class="band-main"></span>
      <span class="band-end"></span>
    </div>
  </section>
</main>
</body>
</html>
```